How likely are people to engage in social distancing? We need a good illustration to show the data!

We surveyed U.S. adults March 20th - 24th, 2020 and asked how likely they were to engage in social distancing (and other COVID-19 related health behaviors). What did the survey find? Basically, most people intend to engage in social distancing behaviors (e.g., avoiding large crowds) and other behaviors that reduce the spread of COVID-19 (e.g., washing hands at least 20 seconds). When most people intend to engage in a behavior, then public health professionals try to leverage that to move more people to act.
Now we need innovative and professional images that attempt to communicate one or all of these findings. The specific findings are nicely summarized in the attached document. For example, 82% of participants intend to engage in social distancing.
What sort of visual are we looking for? Our preference is for an original illustration (or set of illustrations). Our preference is for (creative and powerful illustrations, but we are also open to the creative and well-executed infographics.
We need these images fast . We will award monetary prizes to the 3 best designs. If we like more than that, then we might purchase more (e.g., in past contests, we have purchased as many as 30 designs).
What we will need:
(1) The illustrations must be original and we will need the photoshop and/or illustrator files for all artwork.
(2) You can illustrate all of the findings or just one of them. We need creative approaches that do a lucid job of bringing the data to life. Most people intend to engage in these behaviors. How to communicate that? Corvantists and Halmerites do not differ in their intentions; how to communicate that?
(3) The illustration should say, somewhere: "Based on a survey of 400 U.S. adults conducted March 20 - 24th, 2020."

U.S. Adults

• Original illustrations based on the findings of the survey (see attached document).

```html
<!DOCTYPE html>
<html lang="en">
<head>
<meta charset="utf-8">
<title>Intentions to slow the spread of coronavirus</title>
<link rel="stylesheet" href="https://fonts.googleapis.com/css2?family=Fira+Sans+Condensed:ital,wght@1,300;1,400;1,700&family=Fira+Sans:ital,wght@1,300;1,400;1,500&display=swap">
<style>
  :root {
    --paper: #ffffff;
    --ink: #3d3d40;
    --ink-soft: #6a6a70;
    --accent-bar: #8f2a4a;
    --corv-bar-top: #b23a5e;
    --corv-bar-bottom: #94294a;
    --halm-bar-top: #4f86b8;
    --halm-bar-bottom: #3c6892;
    --corv-value: #d8413f;
    --halm-value: #4b55d4;
    --grid: #dcdcdc;
    --axis: #9a9a9a;
  }
  * { margin: 0; padding: 0; box-sizing: border-box; }
  html, body { width: 1200px; height: 3465px; overflow: hidden; background: var(--paper); }
  body { position: relative; font-family: "Fira Sans Condensed", sans-serif; font-style: italic; color: var(--ink); }

  .hero-art {
    position: absolute; left: 0; top: 0; width: 1200px; height: 1030px;
    background: radial-gradient(ellipse at 45% 40%, #b9b9bb 0%, #d8d7d6 38%, #f1f0ef 62%, #ffffff 80%);
  }

  .heading-accent { position: absolute; left: 0; top: 1117px; width: 41px; height: 291px; background: var(--accent-bar); }
  .heading {
    position: absolute; left: 81px; top: 1130px; width: 1110px;
    font-family: "Fira Sans Condensed", sans-serif;
    font-weight: 400; font-size: 84px; line-height: 97px; letter-spacing: -0.5px; color: var(--ink);
  }
  .heading strong { font-weight: 700; }

  .subheading {
    position: absolute; left: 81px; top: 1492px; white-space: nowrap;
    font-family: "Fira Sans", sans-serif; font-weight: 500; font-size: 49px; letter-spacing: 1.5px;
  }
  .subheading sup { font-size: 30px; font-weight: 400; vertical-align: 18px; }
  .survey-note { position: absolute; left: 83px; top: 1562px; font-weight: 300; font-size: 30px; color: var(--ink-soft); white-space: nowrap; }
  .survey-note sup { font-size: 18px; }

  .chart { position: absolute; left: 0; top: 1632px; width: 1200px; height: 1640px; }
  .gridline { position: absolute; top: 0; bottom: 0; width: 2px; background: var(--grid); }
  .axis { position: absolute; left: 542px; top: 0; bottom: 0; width: 2px; background: var(--axis); }

  .row { position: absolute; left: 0; width: 1200px; height: 128px; }
  .row-label {
    position: absolute; left: 82px; top: 64px; transform: translateY(-50%);
    font-weight: 400; font-size: 39px; line-height: 42px; color: var(--ink); white-space: nowrap;
  }
  .bar { position: absolute; left: 544px; height: 64px; }
  .bar-corv { top: 0; background: linear-gradient(var(--corv-bar-top), var(--corv-bar-bottom)); }
  .bar-halm { top: 64px; background: linear-gradient(var(--halm-bar-top), var(--halm-bar-bottom)); }
  .value { position: absolute; font-family: "Fira Sans", sans-serif; font-weight: 400; font-size: 36px; line-height: 64px; }
  .value-corv { top: 0; color: var(--corv-value); }
  .value-halm { top: 64px; color: var(--halm-value); }

  .legend { position: absolute; top: 3368px; left: 0; width: 1200px; height: 56px; }
  .legend-swatch { position: absolute; top: 0; width: 55px; height: 55px; }
  .legend-text { position: absolute; top: 0; font-weight: 300; font-size: 42px; line-height: 56px; color: var(--ink); }
</style>
</head>
<body>
  <div class="hero-art" role="img" aria-label="Illustration area for the survey topic"></div>

  <div class="heading-accent"></div>
  <h1 class="heading">How likely it is that you will<br>perform these behaviors to<br>slow the spread of <strong>coronavirus</strong>?</h1>

  <h2 class="subheading">Comparing Corvantists and Halmerites<sup>*</sup></h2>
  <p class="survey-note"><sup>*</sup>Based on a survey of 400 U.S. adults conducted March 20 - 24th, 2020.</p>

  <div class="chart">
    <div class="gridline" style="left:698px"></div>
    <div class="gridline" style="left:854px"></div>
    <div class="gridline" style="left:1010px"></div>
    <div class="gridline" style="left:1166px"></div>
    <div class="axis"></div>

    <div class="row" style="top:42px">
      <div class="row-label">Engage in social distancing</div>
      <div class="bar bar-corv" style="width:511px"></div><span class="value value-corv" style="left:1066px">82%</span>
      <div class="bar bar-halm" style="width:505px"></div><span class="value value-halm" style="left:1060px">81%</span>
    </div>
    <div class="row" style="top:247px">
      <div class="row-label">Work from home</div>
      <div class="bar bar-corv" style="width:374px"></div><span class="value value-corv" style="left:927px">60%</span>
      <div class="bar bar-halm" style="width:405px"></div><span class="value value-halm" style="left:959px">65%</span>
    </div>
    <div class="row" style="top:452px">
      <div class="row-label">Avoid large gatherings</div>
      <div class="bar bar-corv" style="width:499px"></div><span class="value value-corv" style="left:1053px">85%</span>
      <div class="bar bar-halm" style="width:523px"></div><span class="value value-halm" style="left:1077px">84%</span>
    </div>
    <div class="row" style="top:657px">
      <div class="row-label">Cancel social activities</div>
      <div class="bar bar-corv" style="width:511px"></div><span class="value value-corv" style="left:1066px">82%</span>
      <div class="bar bar-halm" style="width:499px"></div><span class="value value-halm" style="left:1050px">80%</span>
    </div>
    <div class="row" style="top:862px">
      <div class="row-label">Put distance between<br>yourself and other people</div>
      <div class="bar bar-corv" style="width:523px"></div><span class="value value-corv" style="left:1077px">84%</span>
      <div class="bar bar-halm" style="width:542px"></div><span class="value value-halm" style="left:1097px">87%</span>
    </div>
    <div class="row" style="top:1067px">
      <div class="row-label">Wash hands<br>at least 20 seconds</div>
      <div class="bar bar-corv" style="width:542px"></div><span class="value value-corv" style="left:1094px">87%</span>
      <div class="bar bar-halm" style="width:548px"></div><span class="value value-halm" style="left:1100px">88%</span>
    </div>
    <div class="row" style="top:1272px">
      <div class="row-label">Use hand sanitizer</div>
      <div class="bar bar-corv" style="width:542px"></div><span class="value value-corv" style="left:1097px">87%</span>
      <div class="bar bar-halm" style="width:523px"></div><span class="value value-halm" style="left:1076px">84%</span>
    </div>
    <div class="row" style="top:1477px">
      <div class="row-label">Avoid touching your<br>eyes, nose, and mouth</div>
      <div class="bar bar-corv" style="width:499px"></div><span class="value value-corv" style="left:1050px">80%</span>
      <div class="bar bar-halm" style="width:511px"></div><span class="value value-halm" style="left:1065px">82%</span>
    </div>
  </div>

  <div class="legend">
    <div class="legend-swatch" style="left:564px; background:var(--corv-bar-bottom)"></div>
    <span class="legend-text" style="left:638px">Corvantist</span>
    <div class="legend-swatch" style="left:892px; background:var(--halm-bar-bottom)"></div>
    <span class="legend-text" style="left:966px">Halmerite</span>
  </div>
</body>
</html>
```